Amber Ladle Wishes Website Design; Cupcake Business with a unique and bespoke design element

We need a website design for a new bespoke and unique business making gourmet cupcakes - but MOST IMPORTANTLY we design and handmake cupcake wrappers and toppers specifically for each client's event. We are based in Sydney, Australia. The final resulting website should be elegant yet whimsical reflecting the notion of dreams and very elegant events eg weddings and very special parties.

We want to eventually have about 5 pages, HOWEVER, this project is specifically for the first page (ie Home page) and one other only. The final required pages are: a HOME page; ABOUT US page; PHOTO GALLERY page; FLAVOUR MENU & OTHER PRODUCTS page; CONTACT & INTERNET ENQUIRY page.

We expect the HOME page to be quite elaborate, perhaps including some animation. We will be providing the text content for all the other pages, and basically they will have the same background as the home page. We are looking for a clean design that runs across each page thus giving the website a continuity that pulls it all together. We would like our logo to be included on each page.

PLEASE NOTE: We will want multiple pages worked on in the handover phase but initially we want a very concise, consistent template to limit the amount of work to prospective designers.

While we are primarily looking for the design phase to be covered by this project, we would certainly appreciate coding to be included and will take that into consideration when choosing a winner.

Hi Designers

We have added some more information to our brief - please review it.

Thanks and happy designing

Hi Designers

Please note that we have increased our Prize money to $750.00.  We hope this encourages you to participate.

Thanks and regards
Amber Ladle Wishes

Hi Designers

We've just posted some photos to help give you an idea of what we do.  Please note our attention to detail and precision in our work.

Thanks
Amber Ladle Wishes

Hi Designers

Please Note:  What makes us different  to any other cupcake business is that we design cupcake wrappers and toppers, unique to our client's event whether it be a wedding, a birthday party or product launch.  We consult with our client to understand themes, colours, styles etc.  We then have our designs printed, next they are cut by a specialised computerised cutting machine,  We assemble everything by hand, and usually embellish the wrapper and topper with pearls, crystals, feathers, lace, ribbons or whatever else is appropriate for the event.  All work is totally bespoke, unique and individual.  No other cupcake supplier that we know of goes to these lengths to satisfy their client's dreams.

THE WRAPPER AND TOPPER IS OUR PRIMARY SELLING POINT. 

PLEASE NOTE:- We have uploaded a new photograph which we want to be used as the main photograph on the landing page.

We have removed all previous photographs of cupcakes (except for one that we can't get rid of).

We don't want a picture of a cupcake on the landing page we want the image _D7C3239.jpg to be used for that purpose.

We have also uploaded our logo in a number of file formats as we have had requests from you for these.

Hi designers

we have a crazy busy weekend on and won't be able to make any decisions re our competition until Monday  -  sorry to keep you in suspense, just a couple more days please!

regards
Meg

Target Market(s)

Primarily women - brides, new mothers (Christenings), Event Planners, who place an emphasis on the beauty of a product rather than the cost

Industry/Entity Type

Events

Requirements
Must have
• It must have our Logo (see attached upload) on each page (our logo is a butterfly atop a cupcake resting on a spoon and our motto is "Baked for Your Brightest Days". The colours used are pale pink, blue and chocolate brown and we'd expect these colours to be repeated in the final website.
The website must have a photo gallery which we can access and add to/change as our business grows.
We need a contact page which has an "internet enquiry form".
There should be a "Menu" page describing our cupcake flavours.
The Home page must have a party/event feel to it - definitely making an enquirer want to enter further into the site.
Nice to have
• Our logo is attached below in the "uploads". One idea that we have had is to use the butterfly in the logo but start it as a caterpillar crawling on the screen; as it spins it's cocoon the words "Sweet Dreams Little Caterpillar" would appear on screen; this would incorporate the "Dreams" in our Business Name; then our logo butterfly would hatch. This encapsulates the idea of taking something plain (caterpillar/cupcake) and creating something beautiful (butterfly/OUR cupcake).
However, we are open to other design ideas.
The colours we would like to have are pale pink, blue and chocolate brown in the design.

Some websites we really admire are: www.dorawillow.com www.thimblereedtart.com.au and www.greetingsvera.com.au
These websites have a lightness and sense of fantasy to them. They do not convey a corporate image at all, rather they make you want to be at the party.
Should not have
• No "Corporate" style.

Most Important: We already have a website which we are not happy with - that is why we are going through this exercise to replace it. That means we DO NOT want anything along the lines of our current website. We are expecting some fresh ideas for our prize money.

```html
<!DOCTYPE html>
<html lang="en">
<head>
<meta charset="utf-8">
<title>Amber Ladle Wishes – About Us</title>
<link rel="stylesheet" href="https://fonts.googleapis.com/css2?family=Arimo:wght@400;700&family=Old+Standard+TT&family=Parisienne&display=swap">
<style>
  :root {
    --brown: #634226;
    --brown-text: #5a3b22;
    --pink: #f0609e;
    --pink-heading: #ec5aa4;
    --white: #ffffff;
    --nav-bg: rgba(248, 247, 246, 0.9);
    --icon-bg: #ecebea;
    --icon-edge: #d4d2cf;
  }
  * { box-sizing: border-box; margin: 0; padding: 0; }
  html, body { width: 1200px; height: 896px; overflow: hidden; background: var(--white); }
  body { position: relative; font-family: "Arimo", Arial, sans-serif; color: var(--brown-text); }

  .top-band { position: absolute; left: 0; top: 0; width: 1200px; height: 15px; background: var(--brown); }
  .top-rule { position: absolute; left: 0; top: 15px; width: 1200px; height: 4px; background: var(--pink); }

  .backdrop {
    position: absolute; left: 0; top: 185px; width: 1200px; height: 632px;
    background:
      linear-gradient(180deg, #ffffff 0%, rgba(255,255,255,0) 12%, rgba(255,255,255,0) 80%, #ffffff 100%),
      linear-gradient(90deg, #6f6a63 0%, #b9b1a6 8%, #e6e2dc 20%, #f1efec 50%, #e4e1dc 80%, #a9a59f 92%, #cfcac3 100%);
  }

  .brand { position: absolute; left: 0; top: 62px; width: 1200px; text-align: center; }
  .brand-name {
    display: inline-flex; align-items: center; gap: 12px;
    font-family: "Old Standard TT", Georgia, serif; font-size: 40px; color: var(--brown);
  }
  .brand-dot { width: 14px; height: 14px; border-radius: 50%; background: var(--pink); }
  .brand-motto {
    display: block; margin-top: 8px;
    font-family: "Arimo", Arial, sans-serif; font-size: 12px; color: var(--pink);
  }

  .main-nav {
    position: absolute; left: 106px; top: 201px; width: 989px; height: 56px;
    background: var(--nav-bg); border-radius: 6px 6px 0 0;
  }
  .nav-tab-active {
    position: absolute; left: 82px; top: -6px; width: 111px; height: 59px;
    background: var(--brown); border-radius: 3px 3px 0 0;
  }
  .nav-link {
    position: absolute; top: 18px;
    font-family: "Old Standard TT", Georgia, serif; font-size: 22px; color: var(--brown-text);
    white-space: nowrap;
  }
  .nav-link.is-current { color: var(--white); }
  .social-buttons { position: absolute; left: 813px; top: 10px; display: flex; gap: 14px; }
  .social-button {
    width: 34px; height: 34px; border-radius: 4px;
    background: var(--icon-bg); border: 1px solid var(--icon-edge);
  }

  .content-panel {
    position: absolute; left: 106px; top: 259px; width: 989px; height: 491px;
    background: var(--white); border-radius: 0 0 8px 8px;
  }
  .feature-photo {
    position: absolute; left: 34px; top: 27px; width: 336px; height: 436px;
    background: linear-gradient(160deg, #c3b9a6 0%, #b5ab99 45%, #d9d6d1 70%, #efefed 100%);
  }
  .page-title {
    position: absolute; left: 414px; top: 34px;
    font-family: "Parisienne", cursive; font-size: 44px; font-weight: 400; color: var(--pink-heading);
    line-height: 1;
  }
  .about-copy { position: absolute; left: 418px; top: 96px; width: 502px; }
  .about-copy p {
    font-size: 15px; line-height: 20.3px; letter-spacing: 0.9px; margin-bottom: 20.3px;
  }
  .breadcrumb {
    position: absolute; left: 420px; top: 426px;
    font-size: 15px; letter-spacing: 0.9px; color: var(--pink);
  }
  .breadcrumb span { margin: 0 10px 0 8px; }

  .footer-rule { position: absolute; left: 0; top: 817px; width: 1200px; height: 4px; background: var(--pink); }
  .footer {
    position: absolute; left: 0; top: 821px; width: 1200px; height: 75px; background: var(--brown);
    color: var(--white);
  }
  .copyright {
    position: absolute; left: 0; top: 34px; width: 1200px; text-align: center;
    font-size: 11px; font-weight: 700; letter-spacing: 0.3px;
  }
  .sound-toggle { position: absolute; left: 964px; top: 18px; display: flex; align-items: flex-end; gap: 12px; }
  .sound-label { font-size: 14px; font-weight: 700; padding-bottom: 1px; }
</style>
</head>
<body>
  <div class="top-band"></div>
  <div class="top-rule"></div>

  <div class="backdrop" role="img" aria-label="Soft-focus photograph of lace, paper roses and party decorations"></div>

  <header class="brand">
    <span class="brand-name"><span class="brand-dot"></span>Amber Ladle Wishes</span>
    <span class="brand-motto">Baked for Your Brightest Days</span>
  </header>

  <nav class="main-nav">
    <div class="nav-tab-active"></div>
    <a class="nav-link is-current" style="left:110px">Home</a>
    <a class="nav-link" style="left:216px">About Us</a>
    <a class="nav-link" style="left:343px">Gallery</a>
    <a class="nav-link" style="left:463px">Flavour Menu</a>
    <a class="nav-link" style="left:638px">Contact Us</a>
    <div class="social-buttons">
      <span class="social-button" aria-label="Social page"></span>
      <span class="social-button" aria-label="Social page"></span>
      <span class="social-button" aria-label="Social page"></span>
    </div>
  </nav>

  <main class="content-panel">
    <div class="feature-photo" role="img" aria-label="Photograph of a decorated birthday cupcake with custom wrapper and topper beside a vintage camera and a celebration card"></div>
    <h1 class="page-title">About Us</h1>
    <div class="about-copy">
      <p>Aliquam congue fermentum nisl. Mauris accumsan nulla vel diam. Sed in lacus ut enim adipiscing aliquet.</p>
      <p>Nulla venenatis. In pede mi, aliquet sit amet, euismod in, auctor ut, ligula. Aliquam dapibus tincidunt metus. Praesent justo dolor, lobortis quis, lobortis dignissim, pulvinar ac, lorem. Vestibulum sed ante. Donec sagittis euismod purus.</p>
      <p>Aliquam congue fermentum nisl. Mauris accumsan nulla vel diam. Sed in lacus ut enim adipiscing aliquet.</p>
      <p>Nulla venenatis. In pede mi, aliquet sit amet, euismod in, auctor ut, ligula. Aliquam dapibus tincidunt metus. Praesent justo dolor, lobortis quis, lobortis dignissim, pulvinar ac, lorem. Vestibulum sed ante. Donec sagittis euismod purus.</p>
    </div>
    <div class="breadcrumb">Home<span>|</span>Gallery</div>
  </main>

  <div class="footer-rule"></div>
  <footer class="footer">
    <div class="copyright">© Copyright 2012&nbsp; |&nbsp; Amber Ladle Wishes&nbsp; |&nbsp; All Rights Reserved</div>
    <div class="sound-toggle">
      <svg width="38" height="32" viewBox="0 0 38 32" aria-hidden="true">
        <rect x="0" y="18" width="5" height="14" fill="#ffffff"/>
        <rect x="8" y="12" width="5" height="20" fill="#ffffff"/>
        <rect x="16" y="4" width="5" height="28" fill="#ffffff"/>
        <rect x="24" y="0" width="5" height="32" fill="#ffffff"/>
        <rect x="32" y="8" width="5" height="24" fill="#ffffff"/>
      </svg>
      <span class="sound-label">OFF &nbsp;|&nbsp; ON</span>
    </div>
  </footer>
</body>
</html>
```